Logo and business card for optometric practice
Curtis Hallorann & Associates
Marta Pelovska, O.D.
Oscar Tremwitz, O.D.
Neil Borromi, O.D.
417 Pembrook Parkway
Briarwood Glen, Vermont 11570
516-902-4471

Target Market(s)

Patients, general public

Industry/Entity Type

Business

Logo Text

Curtis Hallorann & Associates Optometrists

Logo styles of interest
Pictorial/Combination Logo
Font styles to use
Serif
Sans Serif

Requirements
Must have
• current inspiration: realistic or photo closeup of eye, with interesting treatment of the iris OR
tech look, with closeup of eye and grid like the doctor is looking through a camera or microscope to view the eye up close
Should not have
• NO cartoons

```html
<!DOCTYPE html>
<html lang="en">
<head>
<meta charset="utf-8">
<title>Curtis Hallorann &amp; Associates — Business Card</title>
<link rel="stylesheet" href="https://fonts.googleapis.com/css2?family=Brawler&family=Arimo:wght@400&display=swap">
<style>
  :root {
    --ink: #0d0d0d;
    --paper: #ffffff;
    --backdrop: #5a5a5a;
    --type-dark: #1a1a1a;
    --type-light: #f2f2f2;
  }
  html, body {
    margin: 0;
    padding: 0;
    width: 1200px;
    height: 741px;
    overflow: hidden;
    background: var(--backdrop);
  }
  .canvas {
    position: relative;
    width: 1200px;
    height: 741px;
    display: flex;
    align-items: center;
    justify-content: center;
    gap: 40px;
  }
  .card {
    width: 520px;
    height: 298px;
    background: var(--paper);
    box-shadow: 0 10px 24px rgba(0,0,0,0.35);
    overflow: hidden;
  }
  .card svg { display: block; width: 520px; height: 298px; }
  .ink { fill: var(--ink); }
  .paper { fill: var(--paper); }
  .brand-curve {
    font-family: "Brawler", serif;
    font-size: 27px;
    fill: var(--type-light);
  }
  .brand-name {
    font-family: "Brawler", serif;
    font-size: 25px;
    fill: var(--type-dark);
  }
  .doctor {
    font-family: "Brawler", serif;
    font-size: 13.5px;
    fill: var(--type-dark);
  }
  .contact {
    font-family: "Arimo", sans-serif;
    font-size: 13px;
    fill: var(--type-light);
    letter-spacing: 0.2px;
  }
</style>
</head>
<body>
<main class="canvas">

  <section class="card card-front" aria-label="Card front">
    <svg viewBox="0 0 520 298" xmlns="http://www.w3.org/2000/svg">
      <defs>
        <path id="front-text-curve" d="M70 262 C 230 225, 380 150, 505 10"/>
      </defs>
      <path class="ink" d="M0 0 H520 V0 C 400 150, 250 250, 0 282 Z"/>
      <circle class="paper" cx="135" cy="130" r="26"/>
      <text class="brand-curve">
        <textPath href="#front-text-curve">Curtis Hallorann &amp; Associates</textPath>
      </text>
    </svg>
  </section>

  <section class="card card-back" aria-label="Card back">
    <svg viewBox="0 0 520 298" xmlns="http://www.w3.org/2000/svg">
      <path class="ink" d="M0 298 C 0 298, 380 270, 520 20 V298 Z"/>
      <circle class="ink" cx="70" cy="95" r="18"/>
      <text class="brand-name" x="40" y="160">Curtis Hallorann</text>
      <text class="brand-name" x="40" y="188">&amp; Associates</text>

      <g class="doctors">
        <text class="doctor" x="300" y="50">Marta Pelovska, O.D.</text>
        <text class="doctor" x="305" y="72">Oscar Tremwitz, O.D.</text>
        <text class="doctor" x="310" y="94">Neil Borromi, O.D.</text>
      </g>

      <g class="contacts">
        <text class="contact" x="330" y="205">417 Pembrook Parkway</text>
        <text class="contact" x="330" y="223">Briarwood Glen, Vermont</text>
        <text class="contact" x="330" y="243">c : 516-902-4471</text>
      </g>
    </svg>
  </section>

</main>
</body>
</html>
```